Business card design Needed for new logo / Construction business, home extensions and new builds

We need a business card design using our new logo files which i will attach to this project :)

We are a small construction business specialising in home extensions, new builds and property development. We are very ambitious and would appreciate professional and elegant designs for our new business card.

Very serious about using the services on BriefNest and recently acquired our new logo from here :)

Please get involved, i will feedback when i can as i am very busy but can respond daily, thanks

Target Market(s)

People that want to build onto their houses, new building developments or adding too their existing property

Industry/Entity Type

Construction

Contact Information for Business Card

Hollin Marsh Construction, Tobias Renwick (Managing Director), Tel 07822200444, email - info@hollin-marsh, www.hollin-marsh.co.uk

Colors

Designer to choose colors to be used in the design.

Requirements
Must have
• I like a deep grey on the back please. A lot of you have provided black from and back, try mixing things up a little. The black looks cool 😎 Thanks

```html
<!DOCTYPE html>
<html lang="en">
<head>
<meta charset="utf-8">
<title>Hollin Marsh Construction – Business Card</title>
<link href="https://fonts.googleapis.com/css2?family=Cinzel:wght@600&family=EB+Garamond:wght@400;500&display=swap" rel="stylesheet">
<style>
  :root {
    --backdrop: #8c8c8c;
    --card-black: #050505;
    --card-grey-1: #2b2b2b;
    --card-grey-2: #1c1c1c;
    --gold-dark: #b98a2e;
    --gold-light: #f2cf7e;
    --silver: #d8d8d8;
    --text-light: #e6e6e6;
  }
  * { margin: 0; padding: 0; box-sizing: border-box; }
  html, body { width: 1200px; height: 900px; overflow: hidden; }
  body {
    background: var(--backdrop);
    position: relative;
    font-family: "EB Garamond", Georgia, serif;
  }
  .card {
    position: absolute;
    left: 250px;
    width: 700px;
    height: 400px;
    overflow: hidden;
    box-shadow: 0 10px 24px rgba(0,0,0,0.35);
  }
  .card-back {
    top: 30px;
    background: radial-gradient(circle at 60% 40%, var(--card-grey-1), var(--card-grey-2));
  }
  .card-front { top: 470px; background: var(--card-black); }
  .corner-art { position: absolute; inset: 0; }

  .back-pattern-area {
    position: absolute; inset: 0;
    background: linear-gradient(135deg, rgba(255,255,255,0.04), rgba(0,0,0,0.1));
  }
  .back-brand {
    position: absolute; right: 56px; top: 178px;
    display: flex; align-items: center; gap: 8px;
    font-family: "Cinzel", Georgia, serif; font-weight: 600;
    font-size: 15px; color: var(--gold-light); letter-spacing: 1px;
  }
  .brand-square { width: 10px; height: 10px; background: var(--gold-light); }

  .front-brand {
    position: absolute; left: 60px; top: 110px;
    display: flex; align-items: center; gap: 12px;
    font-family: "Cinzel", Georgia, serif; font-weight: 600;
    font-size: 25px; line-height: 1.15; color: var(--gold-light); letter-spacing: 1px;
  }
  .front-brand .brand-square { width: 16px; height: 16px; }

  .person { position: absolute; left: 60px; bottom: 48px; }
  .person-name {
    font-family: "Cinzel", Georgia, serif; font-weight: 600;
    font-size: 19px; color: var(--gold-light); letter-spacing: 1px;
  }
  .person-role { font-size: 16px; color: var(--text-light); }

  .contact-list {
    position: absolute; left: 380px; bottom: 64px;
    list-style: none; font-size: 16px; color: var(--text-light);
  }
  .contact-list li { display: flex; align-items: center; gap: 9px; margin-top: 5px; }
  .contact-list svg { width: 14px; height: 14px; fill: var(--gold-light); flex: none; }
</style>
</head>
<body>

<section class="card card-back" aria-label="Card back">
  <div class="back-pattern-area" role="img" aria-label="Subtle tonal background texture"></div>
  <svg class="corner-art" viewBox="0 0 700 400" aria-hidden="true">
    <defs>
      <linearGradient id="goldBack" x1="0" y1="0" x2="1" y2="1">
        <stop offset="0" stop-color="var(--gold-dark)"/>
        <stop offset="0.5" stop-color="var(--gold-light)"/>
        <stop offset="1" stop-color="var(--gold-dark)"/>
      </linearGradient>
    </defs>
    <polygon points="0,60 0,400 310,400" fill="var(--silver)"/>
    <polygon points="0,70 0,400 296,400" fill="url(#goldBack)"/>
    <polygon points="0,140 0,400 230,400" fill="var(--card-black)"/>
  </svg>
  <div class="back-brand"><span class="brand-square"></span>Hollin Marsh</div>
</section>

<section class="card card-front" aria-label="Card front">
  <svg class="corner-art" viewBox="0 0 700 400" aria-hidden="true">
    <defs>
      <linearGradient id="goldFront" x1="0" y1="0" x2="1" y2="1">
        <stop offset="0" stop-color="var(--gold-dark)"/>
        <stop offset="0.5" stop-color="var(--gold-light)"/>
        <stop offset="1" stop-color="var(--gold-dark)"/>
      </linearGradient>
    </defs>
    <polygon points="430,0 700,0 700,320" fill="var(--silver)"/>
    <polygon points="444,0 700,0 700,304" fill="url(#goldFront)"/>
    <polygon points="530,0 700,0 700,200" fill="var(--card-black)"/>
  </svg>

  <div class="front-brand"><span class="brand-square"></span><span>Hollin Marsh<br>Construction</span></div>

  <ul class="contact-list">
    <li><svg viewBox="0 0 16 16"><path d="M3 1h3l1 4-2 1a9 9 0 0 0 5 5l1-2 4 1v3a2 2 0 0 1-2 2A13 13 0 0 1 1 3a2 2 0 0 1 2-2z"/></svg>07822200444</li>
    <li><svg viewBox="0 0 16 16"><path d="M1 3h14v10H1zM2 4l6 5 6-5v1L8 10 2 5z" fill-rule="evenodd"/></svg>info@hollin-marsh.co.uk</li>
    <li><svg viewBox="0 0 16 16"><path d="M8 1a7 7 0 1 0 0 14A7 7 0 0 0 8 1zm0 2a5 5 0 1 1 0 10A5 5 0 0 1 8 3z"/></svg>www.hollin-marsh.co.uk</li>
  </ul>

  <div class="person">
    <p class="person-name">Tobias Renwick</p>
    <p class="person-role">Managing Director</p>
  </div>
</section>

</body>
</html>
```